Business Card Design

We need a business card design for an existing business. Our main trading brand is www.brightmeadowsaver.co.uk

We attach various logo files - please use the version that will produce the sharpest image on the business card.

We are flexible about shape of card etc. Please think outside the box as to what goes on front and what goes on back of the card

We want to be able to amend the card (once the design has been agreed ) to add additional staff details, but the text to go on it will be generic

Details to go on card ( for the first generic one) are fairly minimal as we don't like cluttered business cards:-

Tom Harker
Managing Director

Mobile: 07812 548 207
Email: t.harker@brightmeadowsaver.co.uk

```html
<!DOCTYPE html>
<html lang="en">
<head>
<meta charset="utf-8">
<title>Bright Meadow Saver — Business Card</title>
<link rel="stylesheet" href="https://fonts.googleapis.com/css2?family=Montserrat:wght@300;400;500&display=swap">
<style>
  :root {
    --page: #e4e6ea;
    --card: #f6f6f5;
    --ink: #3b4a60;
    --ink-soft: #8a95a6;
    --brand: #4f6f96;
    --art-blue: #9dbad8;
    --art-lilac: #c9cbe2;
    --tab: #dcdbe8;
  }
  * { box-sizing: border-box; margin: 0; padding: 0; }
  html, body { width: 1200px; height: 900px; overflow: hidden; }
  body {
    background: var(--page);
    font-family: "Montserrat", sans-serif;
    display: flex;
    align-items: center;
    justify-content: center;
    gap: 40px;
  }
  .card {
    position: relative;
    width: 540px;
    height: 327px;
    background: var(--card);
    overflow: hidden;
    box-shadow: 0 6px 20px rgba(40, 50, 70, 0.15);
  }
  .card__art {
    position: absolute;
    right: 0;
    bottom: 0;
    width: 330px;
    height: 230px;
    background: linear-gradient(135deg, rgba(201, 203, 226, 0) 0%, var(--art-lilac) 35%, var(--art-blue) 100%);
    opacity: .55;
  }
  .card__tab {
    position: absolute; left: 0; top: 0;
    width: 120px; height: 30px; background: var(--tab);
  }
  .card__divider {
    position: absolute; left: 130px; top: 0;
    width: 1px; height: 44px; background: var(--ink-soft); opacity: .5;
  }
  .identity { position: absolute; left: 142px; top: 10px; }
  .identity__name {
    font-size: 15px; font-weight: 400; letter-spacing: .5px;
    text-transform: uppercase; color: var(--brand);
  }
  .identity__role {
    font-size: 8px; font-weight: 300; letter-spacing: 1px;
    text-transform: uppercase; color: var(--ink-soft); margin-top: 2px;
  }
  .contact { position: absolute; left: 40px; top: 60px; list-style: none; }
  .contact__item {
    display: flex; align-items: center; gap: 10px;
    font-size: 9px; font-weight: 300; color: var(--ink-soft);
    margin-bottom: 8px;
  }
  .contact__icon { width: 13px; height: 13px; flex: none; }
  .brand-name {
    position: absolute;
    font-size: 31px; font-weight: 500; color: var(--brand);
    letter-spacing: -.5px; white-space: nowrap;
  }
  .card--front .brand-name { left: 30px; top: 118px; }
  .card--back .brand-name { left: 40px; top: 140px; }
</style>
</head>
<body>

  <section class="card card--front" aria-label="Card front">
    <div class="card__art" role="img" aria-label="Decorative graphic of crossing rounded bars in soft blue and lilac"></div>
    <div class="card__tab"></div>
    <div class="card__divider"></div>
    <div class="identity">
      <p class="identity__name">Tom Harker</p>
      <p class="identity__role">Managing Director</p>
    </div>
    <ul class="contact">
      <li class="contact__item">
        <svg class="contact__icon" viewBox="0 0 13 13" aria-label="Mobile"><rect width="13" height="13" rx="1.5" fill="var(--ink)"/><path d="M4 3.5l1.5 0 .6 1.7-.9.7a5 5 0 0 0 2 2l.7-.9 1.6.6v1.5a.8.8 0 0 1-.9.7A6 6 0 0 1 3.3 4.4.8.8 0 0 1 4 3.5z" fill="#fff"/></svg>
        07812 548 207
      </li>
      <li class="contact__item">
        <svg class="contact__icon" viewBox="0 0 13 13" aria-label="Email"><rect width="13" height="13" rx="1.5" fill="var(--ink)"/><rect x="3" y="4" width="7" height="5" fill="#fff"/><path d="M3 4l3.5 3 3.5-3" stroke="var(--ink)" stroke-width=".8" fill="none"/></svg>
        t.harker@brightmeadowsaver.co.uk
      </li>
    </ul>
    <p class="brand-name">brightmeadowsaver.co.uk</p>
  </section>

  <section class="card card--back" aria-label="Card back">
    <div class="card__art" role="img" aria-label="Decorative graphic of crossing rounded bars in soft blue and lilac"></div>
    <p class="brand-name">brightmeadowsaver.co.uk</p>
  </section>

</body>
</html>
```